Stylish Business Card for Modern hair salon

I need a simple business card design using our salon logo and colours that are in the logo. We service clients of all ages but predominantly those in the 18 to 55 age range. We have a young staff and are looking to have a card that will present a modern and clean image that represents who we are. The card should be in black and white same as our logo. Minimal use of other colours is allowed.

Industry/Entity Type

Hair And Beauty

Contact Information for Business Card

The design should have the following information
salon name - TR Hair Studio
address - 2751 Birchfield Rd.E. Mississauga, ON L7P3K2
phone - 905 614-2870
website - trhairexample.ca
instagram - tr.hairstudio
twitter - @TR_HairStudio

Colors
000000
ffffff
474747

Requirements
Must have
• simple design, salon name, address, phone, website, instagram, twitter info
• Back of card should have the following:
• YOUR NEXT APPOINTMENT
• DATE
• TIME
Nice to have
• simple design, clear to see and read,
• predominantly black and white colour, minimal use of other colours is ok
Should not have
• many colours, various fonts

```html
<!DOCTYPE html>
<html lang="en">
<head>
<meta charset="utf-8">
<title>TR Hair Studio – Business Card</title>
<link rel="stylesheet" href="https://fonts.googleapis.com/css2?family=Josefin+Sans:wght@300;400&display=swap">
<style>
  :root {
    --ink: #000000;
    --paper: #ffffff;
    --grey: #474747;
    --edge: #e6e6e6;
  }
  * { margin: 0; padding: 0; box-sizing: border-box; }
  html, body {
    width: 686px;
    height: 1200px;
    overflow: hidden;
    background: var(--ink);
  }
  .canvas {
    position: relative;
    width: 686px;
    height: 1200px;
    background: var(--ink);
    font-family: "Josefin Sans", Arial, sans-serif;
    font-weight: 300;
    color: var(--ink);
  }

  /* Front of card */
  .card-front {
    position: absolute;
    left: 0;
    top: 212px;
    width: 686px;
    height: 392px;
    background: var(--paper);
  }
  .contact {
    position: absolute;
    left: 0;
    top: 0;
    width: 400px;
    height: 392px;
  }
  .contact .phone {
    position: absolute;
    left: 37px;
    top: 16px;
    font-size: 30px;
  }
  .contact .address {
    position: absolute;
    left: 0;
    top: 90px;
    width: 400px;
    text-align: center;
    font-size: 23px;
    line-height: 38px;
  }
  .social {
    position: absolute;
    left: 22px;
    display: flex;
    align-items: center;
    gap: 18px;
    font-size: 20px;
  }
  .social.instagram { top: 272px; }
  .social.twitter { top: 322px; }
  .social-mark {
    display: block;
    width: 22px;
    height: 22px;
    background: var(--ink);
  }
  .social.instagram .social-mark { border-radius: 4px; width: 22px; }
  .social.twitter .social-mark { border-radius: 50%; }

  .brand-panel {
    position: absolute;
    left: 400px;
    top: 0;
    width: 286px;
    height: 392px;
    background: var(--ink);
    border-bottom-left-radius: 8px;
    color: var(--paper);
  }
  .brand-panel .brand-name {
    position: absolute;
    left: 0;
    top: 126px;
    width: 286px;
    text-align: center;
    font-size: 34px;
    font-weight: 400;
    letter-spacing: 1px;
    line-height: 44px;
  }
  .brand-panel .rule {
    position: absolute;
    left: 22px;
    top: 226px;
    width: 242px;
    height: 1px;
    background: var(--paper);
  }
  .brand-panel .website {
    position: absolute;
    left: 0;
    top: 340px;
    width: 286px;
    text-align: center;
    font-size: 20px;
    font-weight: 400;
  }

  /* Back of card */
  .card-back {
    position: absolute;
    left: 0;
    top: 606px;
    width: 686px;
    height: 389px;
    background: var(--paper);
    border-top: 1px solid var(--edge);
  }
  .brand-band {
    position: absolute;
    left: 8px;
    top: 8px;
    width: 670px;
    height: 184px;
    background: var(--ink);
    border-radius: 7px;
    display: flex;
    align-items: center;
    justify-content: center;
    color: var(--paper);
  }
  .brand-band .brand-name {
    font-size: 40px;
    font-weight: 400;
    letter-spacing: 2px;
  }
  .appointment {
    position: absolute;
    left: 42px;
    top: 226px;
    font-size: 30px;
    line-height: 42px;
    color: var(--grey);
    text-transform: uppercase;
  }
</style>
</head>
<body>
  <main class="canvas">
    <section class="card-front">
      <div class="contact">
        <p class="phone">Phone - 905 614-2870</p>
        <p class="address">2751 Birchfield<br>Rd.E. Mississauga, ON L7P3K2</p>
        <p class="social instagram"><span class="social-mark"></span>tr.hairstudio</p>
        <p class="social twitter"><span class="social-mark"></span>@TR_HairStudio</p>
      </div>
      <div class="brand-panel">
        <p class="brand-name">TR Hair Studio</p>
        <span class="rule"></span>
        <p class="website">www.trhairexample.ca</p>
      </div>
    </section>

    <section class="card-back">
      <div class="brand-band">
        <p class="brand-name">TR Hair Studio</p>
      </div>
      <div class="appointment">
        <p>Your next appointment</p>
        <p>Date</p>
        <p>Time</p>
      </div>
    </section>
  </main>
</body>
</html>
```